Environmental Plastics Infographic

We need a series of infographics that can be used individually or as a combined presentation. We'd like the combined piece to include an introduction and conclusion along with 4-5 infographics. Each infographic (information unit) should also work as a standalone. We are trying to help people visualize size proportions and ratios to put carbon footprint/life cycle data for EPS foam packaging in perspective. We are looking for something creative to help people understand what the figures represent in terms they are familiar with.
To view our typical company design/style please see our website at www.trellamark.org. Our primary RGB colors are: (187,140,9); (94,47,29); (94,138,164); and (164,167,15). Secondary RGB colors are (249,162,28) and (218,210,208). Our title/header font is DIN Next LT Pro and our copy font is Calibri 10.5 pt. We can deviate from the font specification if beneficial and welcome interesting text treatments and typography.
We want sufficient white space with easy to grasp message concept with visual components. The attachment showing data points present concepts on how to show the data impacts but are only representative of a baseline concept - we are confident a professional designer can do a much better job with better visual presentation.
Target Market(s)
The audience is international brand manufacturers (brightmoor, kavo), US legislators & government agencies.
Nice to have
- Other creative ideas on how to present this messaging is encouraged.

```html
<!DOCTYPE html>
<html lang="en">
<head>
<meta charset="utf-8">
<title>Trellamark – EPS Life Cycle</title>
<link rel="stylesheet" href="https://fonts.googleapis.com/css2?family=Barlow:wght@400;500;600;700&display=swap">
<style>
  :root{
    --gold:#bb8c09;
    --brown:#5e2f1d;
    --band-blue:#72a4bf;
    --ring-blue:#6f9fbd;
    --green:#a4a70f;
    --navy:#2e4657;
    --white:#ffffff;
  }
  *{box-sizing:border-box;margin:0;padding:0}
  html,body{width:881px;height:1200px;overflow:hidden;background:var(--white)}
  body{font-family:"Barlow",Arial,sans-serif;color:var(--brown)}
  .infographic{position:relative;width:881px;height:1200px;background:var(--white)}
  .abs{position:absolute}

  /* header */
  .brand{position:absolute;left:0;top:62px;width:881px;display:flex;justify-content:center;align-items:center;gap:12px}
  .brand-mark{width:16px;height:16px;border-radius:50%;background:var(--green)}
  .brand-name{font-size:30px;font-weight:500;line-height:1;color:var(--brown);letter-spacing:.5px}

  /* stats band */
  .stats-band{position:absolute;left:0;top:150px;width:881px;height:265px;overflow:hidden}
  .band-shapes{position:absolute;inset:0}
  .diverted-title{left:12px;top:12px;font-size:20px;font-weight:500;color:var(--white);letter-spacing:.6px;white-space:nowrap;line-height:22px}
  .diverted-title .sc{font-size:16px;letter-spacing:1px}
  .diverted-figure{left:8px;top:36px;font-size:78px;font-weight:400;color:var(--white);line-height:70px;letter-spacing:1px}
  .diverted-unit{left:198px;top:107px;font-size:18px;font-weight:500;color:var(--white);letter-spacing:1px;line-height:20px}
  .diverted-rule{left:12px;top:134px;width:258px;height:1.5px;background:var(--white)}
  .household-text{left:128px;top:162px;font-size:15px;line-height:17px;color:var(--brown);letter-spacing:.3px}
  .household-icon{left:80px;top:172px;width:34px;height:48px;background:linear-gradient(var(--brown),#7a4330);border-radius:3px;opacity:.85}
  .used-for{left:316px;top:55px;width:110px;text-align:center;font-size:12.5px;line-height:13.5px;color:var(--brown)}

  .emissions{color:var(--white);font-size:11px;line-height:12px;letter-spacing:.3px}
  .emissions strong{display:block;font-size:14.5px;line-height:15px;font-weight:700;margin-top:6px}
  .emissions-mfg{left:506px;top:18px}
  .emissions-cars{left:506px;top:147px}
  .car-icon{width:88px;height:30px;border-radius:14px 20px 6px 6px;background:var(--navy)}

  /* life cycle circles */
  .cycle{position:absolute;width:367px;height:367px;border:5px solid var(--ring-blue);border-radius:50%}
  .cycle .photo{position:absolute;border-radius:8px}
  .cycle-title{position:absolute;left:0;width:357px;text-align:center;font-size:21px;font-weight:500;line-height:23px;color:var(--ring-blue)}
  .cycle-copy{position:absolute;left:28px;width:301px;text-align:center;font-size:11.5px;line-height:13px;color:var(--gold);letter-spacing:.2px}
  .cycle-note{position:absolute;left:0;width:357px;text-align:center;font-size:12.5px;line-height:14px;color:var(--gold)}
  .metric{position:absolute;font-size:11.5px;font-weight:700;color:var(--green);white-space:nowrap;line-height:13px}
  .metric.light{font-weight:400}
  .metric-box{position:absolute;left:142px;width:74px;height:64px}

  .distance-bar{position:absolute;left:42px;top:98px;width:273px;height:25px;display:flex}
  .distance-bar span{display:flex;align-items:center;justify-content:center;color:var(--white);font-size:10px;font-weight:700}
  .seg-1{width:36px;background:var(--ring-blue)}
  .seg-50{width:96px;background:var(--green)}
  .seg-100{width:141px;background:var(--gold)}
  .distance-label{position:absolute;top:133px;font-size:8.5px;color:var(--brown);white-space:nowrap}

  .feature{position:absolute;left:354px;top:703px;width:192px;height:192px;border-radius:50%;background:var(--green)}
  .feature-label{position:absolute;top:16px;width:100%;text-align:center;color:var(--white);font-size:24px;font-weight:600}
  .feature .photo{position:absolute;left:38px;top:56px;width:118px;height:100px;border-radius:10px;background:linear-gradient(160deg,#ffffff,#dcdcd8)}
</style>
</head>
<body>
<svg width="0" height="0" style="position:absolute" aria-hidden="true">
  <symbol id="open-box" viewBox="0 0 120 100">
    <g fill="none" stroke-width="5" stroke-linejoin="round">
      <polygon points="20,40 60,58 60,97 20,79"/>
      <polygon points="60,58 100,40 100,79 60,97"/>
      <polygon points="20,40 60,58 42,72 2,54"/>
      <polygon points="60,58 100,40 118,54 78,72"/>
      <polygon points="20,40 60,22 42,8 2,26"/>
      <polygon points="60,22 100,40 118,26 78,8"/>
    </g>
  </symbol>
</svg>

<main class="infographic">
  <header class="brand">
    <span class="brand-mark"></span>
    <span class="brand-name">Trellamark</span>
  </header>

  <section class="stats-band">
    <svg class="band-shapes" viewBox="0 0 881 265" width="881" height="265" aria-hidden="true">
      <rect width="881" height="265" fill="var(--band-blue)"/>
      <polygon points="-10,0 456,0 488,130 460,265 -10,265" fill="var(--green)" stroke="var(--white)" stroke-width="5"/>
      <path d="M74 150 q-10 0 -10 10 v34 q0 8 -10 10 q10 2 10 10 v34 q0 10 10 10" fill="none" stroke="var(--brown)" stroke-width="3"/>
      <path d="M258 150 q10 0 10 10 v34 q0 8 10 10 q-10 2 -10 10 v34 q0 10 -10 10" fill="none" stroke="var(--brown)" stroke-width="3"/>
      <g fill="none" stroke="var(--brown)" stroke-width="2.5">
        <rect x="318" y="98" width="30" height="24"/>
        <path d="M322 118 l8 -9 6 6 4 -4 6 7"/>
        <path d="M375 92 a4 4 0 1 1 4 4 v4 l-17 16 h34 l-17 -16"/>
      </g>
      <circle cx="328" cy="105" r="3" fill="var(--brown)"/>
      <circle cx="414" cy="103" r="10" fill="var(--brown)"/>
      <circle cx="407" cy="108" r="7" fill="var(--brown)"/>
      <circle cx="421" cy="108" r="7" fill="var(--brown)"/>
      <rect x="412" y="110" width="4" height="14" fill="var(--brown)"/>
      <path d="M342 148 l30 18 l30 -18" fill="none" stroke="var(--white)" stroke-width="3"/>
      <path d="M429 176 l-12 20 h24 z" fill="none" stroke="var(--white)" stroke-width="2.5"/>
      <text x="429" y="192" fill="var(--white)" font-size="10" font-weight="700" text-anchor="middle" font-family="Barlow, sans-serif">6</text>
      <text x="429" y="210" fill="var(--white)" font-size="10" font-weight="700" text-anchor="middle" font-family="Barlow, sans-serif">PS</text>
      <use href="#open-box" x="296" y="186" width="102" height="86" stroke="var(--white)"/>
      <use href="#open-box" x="396" y="226" width="58" height="48" stroke="var(--white)" opacity=".35"/>
      <use href="#open-box" x="660" y="52" width="38" height="32" stroke="var(--white)"/>
      <circle cx="775" cy="158" r="75" fill="none" stroke="var(--navy)" stroke-width="18"/>
      <circle cx="775" cy="158" r="75" fill="none" stroke="var(--white)" stroke-width="18" stroke-dasharray="28 460" transform="rotate(-112 775 158)"/>
    </svg>

    <h1 class="abs diverted-title">EPS <span class="sc">DIVERTED FROM THE LANDFILL IN 2018</span></h1>
    <div class="abs diverted-figure">19,850</div>
    <div class="abs diverted-unit">TONS</div>
    <div class="abs diverted-rule"></div>
    <div class="abs household-icon" role="img" aria-label="Pictogram of a person dropping waste into a bin"></div>
    <p class="abs household-text">The equivalent of<br>waste generated<br>by <strong>13,233</strong><br>U.S. households</p>
    <p class="abs used-for">This EPS was<br>used to make:</p>

    <p class="abs emissions emissions-mfg">EPS U.S. manufacturing in<br>2017 was 6.35 million tons<br>Each ton of EPS production<br>emits .5360 kg/tn CO2<strong>Total CO2 impact =<br>3.5 million tons</strong></p>
    <p class="abs emissions emissions-cars">272.48 million cars<br>registered in the U.S. in 2017<br>Each car emits an average<br>of 7 tns of CO2/year<strong>Total CO2 impact =<br>1.907 billion tons</strong></p>
    <div class="abs car-icon" style="left:731px;top:119px" role="img" aria-label="Car icon"></div>
    <div class="abs car-icon" style="left:731px;top:166px" role="img" aria-label="Car icon"></div>
  </section>

  <section class="cycle" style="left:27px;top:430px">
    <div class="photo" style="left:110px;top:20px;width:130px;height:62px;background:linear-gradient(160deg,#f06a2a,#c0401a 70%,#f3f3f3)" role="img" aria-label="Photo of an orange sports sedan"></div>
    <div class="distance-bar"><span class="seg-1">1 km</span><span class="seg-50">50 km</span><span class="seg-100">100 km</span></div>
    <span class="distance-label" style="left:16px">115.5 kg CO2</span>
    <span class="distance-label" style="left:112px">5,775 kg CO2</span>
    <span class="distance-label" style="left:252px">11,550 kg CO2</span>
    <h2 class="cycle-title" style="top:157px">EPS Life Cycle – Global Warming</h2>
    <p class="cycle-copy" style="top:196px">EPS has a very low global warming impact compared to other packaging materials. The carbon footprint for manufacturing 1 ton of EPS is the equivalent of driving your car 31 miles.</p>
    <span class="metric" style="left:56px;top:282px">1 ton of EPS</span>
    <svg class="metric-box" style="top:264px" aria-hidden="true"><use href="#open-box" width="74" height="64" stroke="var(--green)"/></svg>
    <span class="metric" style="left:226px;top:282px">5,360 kg CO2</span>
  </section>

  <section class="cycle" style="left:490px;top:430px">
    <div class="photo" style="left:140px;top:10px;width:96px;height:104px;border-radius:50% 50% 20% 20%;background:radial-gradient(circle at 55% 40%,#fff5c8,#e8b44a 55%,#b98f4a)" role="img" aria-label="Photo of a glowing filament lightbulb"></div>
    <p class="cycle-note" style="top:130px">One 100 watt lightbulb = 360 MJ</p>
    <h2 class="cycle-title" style="top:157px">Life Cycle – Non-Renewable<br>Energy Use</h2>
    <p class="cycle-copy" style="top:216px">EPS energy consumption for the manufacture of 1 ton of packaging material is equivalent to 300 hours of light for a single lightbulb.</p>
    <span class="metric" style="left:56px;top:282px">1 ton of EPS</span>
    <svg class="metric-box" style="top:264px" aria-hidden="true"><use href="#open-box" width="74" height="64" stroke="var(--green)"/></svg>
    <span class="metric" style="left:232px;top:282px">108,000 MJ</span>
  </section>

  <section class="cycle" style="left:27px;top:812px">
    <div class="photo" style="left:98px;top:26px;width:150px;height:92px;background:linear-gradient(150deg,#9fd8f2,#2e9ad4 60%,#6f7b80)" role="img" aria-label="Photo of a rectangular swimming pool"></div>
    <p class="cycle-note" style="top:142px">24,000 gallons<br>One 40x20 foot swimming pool (avg 4 ft depth)</p>
    <h2 class="cycle-title" style="top:190px">Life Cycle – Water Consumption</h2>
    <p class="cycle-copy" style="top:222px">The amount of water used to manufacture 1,000 EPS shipping containers is the equivalent of xx swimming pools.</p>
    <span class="metric" style="left:58px;top:286px">1 ton of EPS</span>
    <svg class="metric-box" style="top:268px" aria-hidden="true"><use href="#open-box" width="74" height="64" stroke="var(--ring-blue)"/></svg>
    <span class="metric" style="left:232px;top:286px">108,000 MJ</span>
  </section>

  <section class="cycle" style="left:490px;top:812px">
    <div class="photo" style="left:130px;top:24px;width:98px;height:104px;background:linear-gradient(160deg,#d8b68a,#b08556 70%,#8a6440)" role="img" aria-label="Photo of stacked corrugated cardboard boxes"></div>
    <p class="cycle-note" style="top:158px">uses xxx gallons of water</p>
    <h2 class="cycle-title" style="top:190px">Life Cycle Water Consumption</h2>
    <p class="cycle-copy" style="top:222px">The amount of water used to manufacture 1,000 EPS shipping containers is a miniscule amount compared to corrugated paper.</p>
    <span class="metric light" style="left:56px;top:286px">1 ton of EPS</span>
    <svg class="metric-box" style="top:268px" aria-hidden="true"><use href="#open-box" width="74" height="64" stroke="var(--green)"/></svg>
    <span class="metric light" style="left:222px;top:286px;text-align:center">uses xxx gallons<br>of water</span>
  </section>

  <section class="feature">
    <div class="feature-label">EPS</div>
    <div class="photo" role="img" aria-label="Photo of white moulded EPS foam packaging pieces"></div>
  </section>
</main>
</body>
</html>
```